a save the date design that can also be used for an invitation

We want to use the name 'Jo'
Also a subtle nod to the Fernbridge Rovers logo
Also very small illustrations so indicate food (a burger or pizza), drinks (cocktail) and dancing (musical notes).
Also a small scroll.

Once we see the detail we can think how to space them so I can use them on paperless post.

The style needs to be modern, suitable for a 12 year old boy and colours only blues and white.

```html
<!DOCTYPE html>
<html lang="en">
<head>
<meta charset="utf-8">
<title>Save the Date – Jo</title>
<link rel="stylesheet" href="https://fonts.googleapis.com/css2?family=Barlow+Condensed:ital,wght@0,100;0,500;0,800;1,400;1,700&family=Barlow:wght@500&display=swap">
<style>
  :root {
    --navy: #1e2456;
    --sky: #2aa9e0;
    --royal: #0a6fd6;
    --paper: #ffffff;
    --frame-grey: #c8c9d6;
    --ice: #dbe8f7;
    --floor: #e6e7ec;
  }
  html, body {
    margin: 0;
    padding: 0;
    width: 1200px;
    height: 800px;
    overflow: hidden;
    background: var(--navy);
  }
  .invitation {
    position: relative;
    width: 1200px;
    height: 800px;
    background: var(--navy);
  }
  .invitation svg {
    position: absolute;
    inset: 0;
  }
  .headline-bold {
    font-family: "Barlow Condensed", sans-serif;
    font-weight: 800;
    fill: var(--sky);
  }
  .headline-thin {
    font-family: "Barlow Condensed", sans-serif;
    font-weight: 100;
    fill: var(--royal);
  }
  .monogram {
    font-family: "Barlow Condensed", sans-serif;
    font-weight: 800;
    fill: var(--paper);
  }
  .date-text {
    font-family: "Barlow", sans-serif;
    font-weight: 500;
    fill: var(--sky);
  }
  .venue-line {
    font-family: "Barlow Condensed", sans-serif;
    font-style: italic;
    font-weight: 400;
    fill: var(--navy);
  }
  .venue-line .accent {
    font-weight: 700;
    fill: var(--sky);
  }
  .music-notes {
    fill: var(--sky);
  }
  .party-icons {
    fill: none;
    stroke: var(--sky);
    stroke-width: 1.8;
    stroke-linecap: round;
    stroke-linejoin: round;
  }
  .party-icons .dot {
    fill: var(--sky);
    stroke: none;
  }
</style>
</head>
<body>
<main class="invitation">
  <svg width="1200" height="800" viewBox="0 0 1200 800" xmlns="http://www.w3.org/2000/svg">
    <defs>
      <linearGradient id="dancer-tones" x1="0" y1="0" x2="0" y2="1">
        <stop offset="0" stop-color="#eef4fb"/>
        <stop offset="0.5" stop-color="#d3e3f5"/>
        <stop offset="1" stop-color="#b9c8e4"/>
      </linearGradient>
      <symbol id="note-single" viewBox="0 0 16 30">
        <ellipse cx="6" cy="25" rx="5.5" ry="4" transform="rotate(-20 6 25)"/>
        <rect x="9.6" y="2" width="2.2" height="23"/>
        <path d="M11.8 2 Q12 9 16 12 Q13 8 11.8 7 Z"/>
      </symbol>
      <symbol id="note-double" viewBox="0 0 30 32">
        <ellipse cx="6" cy="27" rx="5.5" ry="4" transform="rotate(-20 6 27)"/>
        <ellipse cx="23" cy="23" rx="5.5" ry="4" transform="rotate(-20 23 23)"/>
        <rect x="9.6" y="6" width="2.2" height="21"/>
        <rect x="26.6" y="2" width="2.2" height="21"/>
        <polygon points="9.6,6 28.8,2 28.8,7 9.6,11"/>
      </symbol>
    </defs>

    <!-- card -->
    <rect class="card" x="68" y="54" width="1064" height="700" fill="var(--paper)"/>

    <!-- corner accents -->
    <g class="corner-accents" fill="var(--sky)">
      <polygon points="68,54 218,54 68,204"/>
      <polygon points="972,54 1132,54 1132,214"/>
      <polygon points="68,604 68,754 218,754"/>
      <polygon points="1132,594 1132,754 972,754"/>
    </g>

    <!-- inner frame -->
    <rect class="inner-frame-blue" x="114" y="96" width="972" height="614" fill="none" stroke="var(--royal)" stroke-opacity="0.35" stroke-width="4"/>
    <line class="inner-frame-rule" x1="112" y1="94" x2="1088" y2="94" stroke="var(--frame-grey)" stroke-width="4"/>
    <line class="inner-frame-rule" x1="112" y1="712" x2="1088" y2="712" stroke="var(--frame-grey)" stroke-width="4"/>

    <!-- headline -->
    <text class="headline-bold" x="228" y="272" font-size="170" textLength="304" lengthAdjust="spacingAndGlyphs">SAVE</text>
    <circle class="monogram-disc" cx="380" cy="352" r="128" fill="var(--navy)" fill-opacity="0.92"/>
    <text class="headline-thin" x="232" y="408" font-size="167" textLength="296" lengthAdjust="spacingAndGlyphs">THE</text>
    <text class="headline-bold" x="230" y="544" font-size="170" textLength="304" lengthAdjust="spacingAndGlyphs">DATE</text>
    <text class="monogram" x="380" y="395" font-size="130" text-anchor="middle">Jo</text>

    <!-- date -->
    <rect class="date-banner" x="232" y="568" width="302" height="54" fill="var(--navy)"/>
    <text class="date-text" x="383" y="607" font-size="30" text-anchor="middle">20<tspan font-size="17" dy="-12">th</tspan><tspan dy="12"> March 2026</tspan></text>

    <!-- venue -->
    <text class="venue-line" x="232" y="663" font-size="27" textLength="306" lengthAdjust="spacingAndGlyphs">@ THE <tspan class="accent">LOREM</tspan> - <tspan class="accent">6pm</tspan> ONWARDS</text>

    <!-- dancer -->
    <ellipse class="dancer-floor" cx="718" cy="656" rx="118" ry="7" fill="var(--floor)"/>
    <rect class="dancer-illustration" role="img" aria-label="Illustration of a boy dancing" x="636" y="204" width="196" height="448" rx="12" fill="url(#dancer-tones)"/>

    <!-- musical notes -->
    <g class="music-notes">
      <use href="#note-double" x="572" y="156" width="26" height="28"/>
      <use href="#note-single" x="646" y="156" width="12" height="24"/>
      <use href="#note-single" x="734" y="156" width="12" height="24"/>
      <use href="#note-single" x="822" y="156" width="12" height="24"/>
      <use href="#note-double" x="678" y="198" width="26" height="28"/>
      <use href="#note-single" x="588" y="230" width="16" height="30"/>
      <use href="#note-single" x="668" y="268" width="16" height="30"/>
      <use href="#note-single" x="806" y="272" width="12" height="24"/>
      <use href="#note-double" x="598" y="296" width="26" height="30"/>
    </g>

    <!-- party icons -->
    <g class="party-icons">
      <g class="icon-burger" role="img" aria-label="Burger icon">
        <path d="M892 204 Q892 164 936 164 Q980 164 980 204 Z"/>
        <circle class="dot" cx="918" cy="182" r="2"/>
        <circle class="dot" cx="936" cy="176" r="2"/>
        <circle class="dot" cx="954" cy="184" r="2"/>
        <path d="M890 212 Q898 206 906 212 T922 212 T938 212 T954 212 T970 212 T984 210"/>
        <rect x="892" y="216" width="90" height="10" rx="4"/>
        <path d="M898 230 L980 226 Q982 240 960 240 L910 240 Q896 240 898 230 Z"/>
      </g>
      <g class="icon-drink" role="img" aria-label="Drink icon">
        <path d="M898 318 L966 306 L962 378 Q962 384 956 384 L912 386 Q906 386 906 380 Z"/>
        <line x1="906" y1="328" x2="962" y2="320"/>
        <line x1="904" y1="300" x2="918" y2="340"/>
        <circle cx="956" cy="300" r="11"/>
        <line x1="945" y1="300" x2="967" y2="300"/>
        <rect x="918" y="342" width="14" height="14" rx="2"/>
        <rect x="936" y="338" width="14" height="14" rx="2"/>
        <rect x="926" y="358" width="14" height="14" rx="2"/>
      </g>
      <g class="icon-pizza" role="img" aria-label="Pizza slice icon">
        <path d="M892 506 L968 436 Q986 440 984 456 Z"/>
        <path d="M968 436 Q992 434 986 456"/>
        <circle cx="936" cy="478" r="5"/>
        <circle cx="958" cy="462" r="4"/>
        <circle cx="912" cy="494" r="4"/>
        <circle class="dot" cx="950" cy="480" r="1.8"/>
      </g>
      <g class="icon-cocktail" role="img" aria-label="Cocktail glass icon">
        <path d="M906 552 L976 566 L934 604 Z"/>
        <line x1="934" y1="604" x2="928" y2="652"/>
        <path d="M908 660 Q928 648 948 660"/>
        <circle cx="950" cy="552" r="8"/>
        <line x1="956" y1="546" x2="962" y2="540"/>
        <circle class="dot" cx="922" cy="566" r="1.6"/>
        <circle class="dot" cx="932" cy="574" r="1.6"/>
      </g>
    </g>
  </svg>
</main>
</body>
</html>
```